Specialized Personal Trainer Needs a Business Card Design

I need a business card design for my personal training business called Tall Oak Fitness. I have my Human Kinetics degree in Exercise Science from the Halvern Ridge University as well as an extra certification from NBEP (National Board of Exercise Practice). I work as a Cardiac Rehab Exercise Specialist and personal trainer giving specialized exercise prescriptions to those that have different heart conditions as well as work with the general population in weight loss, strength and conditioning, getting/staying fit.
Updates

I decided that I wanted a logo (as I did not have one before I submitted my project for a business card) so I am submitting a project to get a logo done and then I will decide on a business card, hopefully being able to use one of the designs already submitted.  My apologies for doing this backwards.  I am new to this so I appreciate your patience.

Thank you.

Hi, I have just created a project for a logo design (I realized I needed a logo and I should've done that first..oops!), please feel free to participate.  Once I receive a logo I like I will finalize my business card project and hopefully incorporate it into one of your business card designs. 

Thank you!

Target Market(s)

Business professionals

Industry/Entity Type

Personal Trainer

Requirements
Must have
• My name with my info:
Celia R. Dunhill (BHK)
NBEP Certified Clinical Exercise Specialist & Personal Trainer
celia.dunhill@talloakfitness.example
Cell: 604-358-4170

Please make it double sided.
Nice to have
• An image that represents cardiac and general fitness training.

```html
<!DOCTYPE html>
<html lang="en">
<head>
<meta charset="utf-8">
<title>Tall Oak Fitness — Business Card</title>
<link href="https://fonts.googleapis.com/css2?family=Didact+Gothic&display=swap" rel="stylesheet">
<style>
  :root {
    --backdrop: #2e2e2e;
    --card: #f4f4f4;
    --card-shade: #e6e6e6;
    --ink: #5a5a5a;
    --ink-soft: #8a8a8a;
    --ink-faint: #c4c4c4;
    --rule: #9a9a9a;
    --heart-red: #e0201c;
  }
  * { margin: 0; padding: 0; box-sizing: border-box; }
  html, body {
    width: 1200px; height: 800px; overflow: hidden;
    background: var(--backdrop);
    font-family: "Didact Gothic", "Century Gothic", sans-serif;
    color: var(--ink);
  }
  .canvas {
    width: 1200px; height: 800px;
    display: flex; align-items: center; justify-content: center; gap: 40px;
  }
  .card {
    position: relative;
    width: 540px; height: 309px;
    background: linear-gradient(135deg, #ffffff 0%, var(--card) 55%, var(--card-shade) 100%);
    box-shadow: 0 10px 30px rgba(0,0,0,.45);
  }

  /* ---------- Back: contact side ---------- */
  .card--contact .brand-panel {
    position: absolute; left: 0; top: 0; bottom: 0; width: 46%;
    display: flex; flex-direction: column; align-items: center; justify-content: center; gap: 14px;
  }
  .brand-dot {
    width: 46px; height: 46px; border-radius: 50%;
    background: var(--heart-red);
  }
  .brand-name-small { font-size: 18px; letter-spacing: .5px; color: var(--ink-soft); }
  .divider {
    position: absolute; left: 46%; top: 0; bottom: 0; width: 1px;
    background: var(--card-shade);
  }
  .contact-panel {
    position: absolute; left: 51%; right: 22px; top: 74px;
  }
  .person-name { font-size: 18px; color: var(--ink-soft); letter-spacing: .3px; }
  .person-title { font-size: 7.5px; color: var(--ink-soft); margin-top: 5px; letter-spacing: .2px; }
  .contact-list { list-style: none; margin-top: 34px; display: flex; flex-direction: column; gap: 9px; }
  .contact-item { display: flex; align-items: center; gap: 8px; font-size: 11.5px; color: var(--ink-soft); }
  .contact-icon { width: 12px; height: 12px; flex: none; }

  /* ---------- Front: brand side ---------- */
  .card--brand .brand-row {
    position: absolute; left: 60px; right: 40px; top: 100px;
    display: flex; align-items: center; gap: 24px;
  }
  .brand-dot--large { width: 70px; height: 70px; }
  .brand-text { flex: 1; }
  .brand-name { font-size: 33px; color: var(--ink); letter-spacing: .5px; line-height: 1; }
  .tagline {
    display: flex; align-items: center; gap: 8px; margin-top: 8px;
    font-size: 9.5px; font-weight: 700; color: var(--ink-soft); letter-spacing: .4px;
  }
  .tagline::before, .tagline::after {
    content: ""; flex: 1; height: 1px; background: var(--rule);
  }
  .website {
    position: absolute; left: 0; right: 0; bottom: 40px; text-align: center;
    font-size: 15px; color: var(--ink-faint); letter-spacing: 1px;
  }
</style>
</head>
<body>
<main class="canvas">

  <section class="card card--contact" aria-label="Card back with contact details">
    <div class="brand-panel">
      <span class="brand-dot" aria-hidden="true"></span>
      <span class="brand-name-small">Tall Oak Fitness</span>
    </div>
    <div class="divider" aria-hidden="true"></div>
    <div class="contact-panel">
      <h1 class="person-name">Celia R. Dunhill (BHK)</h1>
      <p class="person-title">NBEP Certified Clinical Exercise Specialist &amp; Personal Trainer</p>
      <ul class="contact-list">
        <li class="contact-item">
          <svg class="contact-icon" viewBox="0 0 12 12" aria-hidden="true">
            <rect x="1" y="3" width="10" height="7" fill="none" stroke="#777" stroke-width="1"/>
            <path d="M1 3 L6 7 L11 3" fill="none" stroke="#777" stroke-width="1"/>
          </svg>
          celia.dunhill@talloakfitness.example
        </li>
        <li class="contact-item">
          <svg class="contact-icon" viewBox="0 0 12 12" aria-hidden="true">
            <rect x="3" y="1" width="6" height="10" rx="1" fill="#777"/>
            <rect x="4" y="2.5" width="4" height="5" fill="#eee"/>
          </svg>
          604-358-4170
        </li>
      </ul>
    </div>
  </section>

  <section class="card card--brand" aria-label="Card front with brand name">
    <div class="brand-row">
      <span class="brand-dot brand-dot--large" aria-hidden="true"></span>
      <div class="brand-text">
        <p class="brand-name">Tall Oak Fitness</p>
        <p class="tagline">Your Cardiac Fitness Specialist</p>
      </div>
    </div>
    <p class="website">www.talloakfitness.example</p>
  </section>

</main>
</body>
</html>
```